BRIGHTFIELD BUILDERS leave behind sales FLYER 8.5"x11"

We need a high quality advertising flyer 8.5"x11" for our construction company offering kitchen and bathroom remodels. Can be front and back or just the front of the flyer depending on the design. phone number to come
www.tarnwickbuildco.example

we are also a home inspection company. We will leave this at the home when we are done with our home inspections for our new home owners

Target Market(s)

Home owners

Industry/Entity Type

Residential Construction

Contact Information for Business Card

We want it to match the flyer please

Requirements
Must have
• My logo, my website , my phone number (to come later),
• FL State Lic. #RBQ4807193 & Insured
• We Specialize in Bathroom and Kitchen remodeling ,new Construction & Interior or Exterior home Renovations, garages and more! Serving Central Florida for over 15 years.
• Family owned and operated,
• we perform all levels of building and remodeling.
• i wouldn't mind seeing what you come up with for text on the flyer.
Nice to have
• maybe a nice kitchen and bathroom pictures

```html
<!DOCTYPE html>
<html lang="en">
<head>
<meta charset="utf-8">
<title>Brightfield Builders Flyer</title>
<link href="https://fonts.googleapis.com/css2?family=Roboto+Condensed:ital,wght@0,400;0,700;1,700&family=Cabin:wght@400;500&display=swap" rel="stylesheet">
<style>
  :root{
    --orange:#f39325;
    --charcoal:#2f3540;
    --ink:#2b2f36;
    --body:#4a4d52;
    --panel:#e6e6e7;
    --logo-panel:#e9e9ea;
    --white:#ffffff;
  }
  *{margin:0;padding:0;box-sizing:border-box}
  html,body{width:1054px;height:1200px;overflow:hidden;background:var(--white)}
  .flyer{position:relative;width:1054px;height:1200px;overflow:hidden;background:var(--white);font-family:'Cabin',sans-serif;color:var(--body)}
  .abs{position:absolute}
  .hero-photo{left:0;top:0;width:1054px;height:608px;
    background:linear-gradient(160deg,#d9d6d0 0%,#eeece8 30%,#c9c4bd 55%,#6b5a4a 80%,#4a3a2e 100%)}
  .shapes{left:0;top:0;width:1054px;height:1200px}
  .brand{left:28px;top:60px;width:400px;text-align:center;font-family:'Roboto Condensed',sans-serif;font-weight:700;color:#3a3d42}
  .brand-mark{display:block;width:62px;height:62px;margin:0 auto 18px;background:var(--orange)}
  .brand-name{display:block;font-size:34px;letter-spacing:2px;line-height:1}
  .brand-sub{display:block;font-size:19px;letter-spacing:14px;margin-top:10px;padding-left:14px}
  .tagline{left:425px;top:64px;width:600px;font-family:'Roboto Condensed',sans-serif;font-style:italic;font-weight:700;font-size:21px;color:var(--ink);letter-spacing:.3px}
  .guarantee{left:33px;top:592px;font-size:28px;color:var(--white);font-family:'Cabin',sans-serif;letter-spacing:.3px}
  .accent{color:var(--orange)}
  .headline{left:32px;top:682px;width:580px;font-family:'Roboto Condensed',sans-serif;font-weight:700;font-size:28px;line-height:33px;color:var(--ink);text-transform:uppercase}
  .intro{left:32px;top:834px;width:470px;font-size:18.5px;line-height:24.5px}
  .services{left:32px;top:958px;display:grid;grid-template-columns:228px 200px;row-gap:6px;list-style:none;font-size:18.5px;line-height:23px}
  .services li{display:flex;align-items:center;gap:9px}
  .services svg{width:17px;height:17px;flex:none}
  .license{left:36px;top:1094px;font-size:13px;color:#3a3d42;letter-spacing:-.2px}
  .bath-photo{left:0;top:0}
  .choice{left:600px;top:902px;width:426px;text-align:center}
  .choice-title{font-family:'Roboto Condensed',sans-serif;font-weight:700;font-size:26px;line-height:33px;color:var(--ink);text-transform:uppercase}
  .choice-text{margin-top:14px;font-size:18.5px;line-height:24.5px}
  .phone{left:32px;top:1128px;display:flex;align-items:center;gap:12px;font-family:'Roboto Condensed',sans-serif;font-weight:700;font-size:32px;color:var(--white)}
  .phone svg{width:34px;height:34px}
  .footer-links{left:571px;top:1158px;display:flex;align-items:center}
  .social-square{width:22px;height:22px;background:var(--orange);margin-right:18px}
  .website{margin-left:18px;font-size:21px;letter-spacing:3.4px;color:var(--white)}
</style>
</head>
<body>
<main class="flyer">
  <div class="abs hero-photo" role="img" aria-label="Photo of a bright modern kitchen with white island, bar stools and dark cabinetry"></div>

  <svg class="abs shapes" viewBox="0 0 1054 1200" aria-hidden="true">
    <polygon points="0,0 459,0 366,216 0,216" fill="var(--logo-panel)" opacity=".95"/>
    <polygon points="415,53 1054,53 1054,105 395,105" fill="#ffffff" opacity=".55"/>
    <polygon points="992,0 1054,0 1054,608 750,608" fill="var(--orange)" opacity=".45"/>
    <polygon points="0,576 560,576 589,647 0,647" fill="var(--charcoal)"/>
    <polygon points="505,666 589,647 540,647" fill="var(--orange)"/>
    <polygon points="601,868 1054,868 1054,1136 463,1136" fill="var(--panel)"/>
    <polygon points="400,1136 1054,1136 1054,1200 366,1200" fill="var(--charcoal)"/>
    <polygon points="0,1119 400,1119 367,1177 0,1177" fill="var(--orange)"/>
  </svg>

  <svg class="abs bath-photo" width="1054" height="860" viewBox="0 0 1054 860" role="img" aria-label="Photo of a modern grey tiled bathroom with basin, toilet and glass shower">
    <defs>
      <linearGradient id="bathTones" x1="0" y1="0" x2="1" y2="1">
        <stop offset="0" stop-color="#6d6f72"/>
        <stop offset=".5" stop-color="#b4b5b7"/>
        <stop offset="1" stop-color="#5c5e61"/>
      </linearGradient>
    </defs>
    <polygon points="694,648 1054,648 1054,852 611,852" fill="url(#bathTones)"/>
  </svg>

  <div class="abs brand">
    <span class="brand-mark"></span>
    <span class="brand-name">BRIGHTFIELD</span>
    <span class="brand-sub">BUILDERS</span>
  </div>

  <p class="abs tagline">SERVING CENTRAL FLORIDA FOR OVER 15 YEARS.</p>

  <p class="abs guarantee">Quality Construction <span class="accent">Guaranteed!</span></p>

  <h1 class="abs headline">We specialize in new construction &amp;<br><span class="accent">interior or exterior home renovations,</span><br>including bathroom and kitchen<br>remodeling, garages and more!</h1>

  <p class="abs intro">Family owned and operated, we perform all levels of building and remodeling. We offer start-to-finish solutions for every project. We guarantee high quality construction for each and every project.</p>

  <ul class="abs services">
    <li><svg viewBox="0 0 17 17"><rect x="1" y="3" width="12" height="12" fill="none" stroke="#9a9ca0" stroke-width="1.4"/><path d="M4 9l3 3 9-10" fill="none" stroke="#9a9ca0" stroke-width="1.6"/></svg>New Construction</li>
    <li><svg viewBox="0 0 17 17"><rect x="1" y="3" width="12" height="12" fill="none" stroke="#9a9ca0" stroke-width="1.4"/><path d="M4 9l3 3 9-10" fill="none" stroke="#9a9ca0" stroke-width="1.6"/></svg>Repairs</li>
    <li><svg viewBox="0 0 17 17"><rect x="1" y="3" width="12" height="12" fill="none" stroke="#9a9ca0" stroke-width="1.4"/><path d="M4 9l3 3 9-10" fill="none" stroke="#9a9ca0" stroke-width="1.6"/></svg>Barns</li>
    <li><svg viewBox="0 0 17 17"><rect x="1" y="3" width="12" height="12" fill="none" stroke="#9a9ca0" stroke-width="1.4"/><path d="M4 9l3 3 9-10" fill="none" stroke="#9a9ca0" stroke-width="1.6"/></svg>Kitchens</li>
    <li><svg viewBox="0 0 17 17"><rect x="1" y="3" width="12" height="12" fill="none" stroke="#9a9ca0" stroke-width="1.4"/><path d="M4 9l3 3 9-10" fill="none" stroke="#9a9ca0" stroke-width="1.6"/></svg>Remodels</li>
    <li><svg viewBox="0 0 17 17"><rect x="1" y="3" width="12" height="12" fill="none" stroke="#9a9ca0" stroke-width="1.4"/><path d="M4 9l3 3 9-10" fill="none" stroke="#9a9ca0" stroke-width="1.6"/></svg>Bathrooms</li>
    <li><svg viewBox="0 0 17 17"><rect x="1" y="3" width="12" height="12" fill="none" stroke="#9a9ca0" stroke-width="1.4"/><path d="M4 9l3 3 9-10" fill="none" stroke="#9a9ca0" stroke-width="1.6"/></svg>Renovations</li>
    <li><svg viewBox="0 0 17 17"><rect x="1" y="3" width="12" height="12" fill="none" stroke="#9a9ca0" stroke-width="1.4"/><path d="M4 9l3 3 9-10" fill="none" stroke="#9a9ca0" stroke-width="1.6"/></svg>Garages</li>
  </ul>

  <p class="abs license">FL State Lic. #RBQ4807193 &amp; Insured</p>

  <section class="abs choice">
    <h2 class="choice-title">We're the <span class="accent">best choice</span> for<br>your home renovation project.</h2>
    <p class="choice-text">Family owned and operated, we perform all levels of building and remodeling. We offer start-to-finish solutions for every project. We also offer full design services.</p>
  </section>

  <div class="abs phone">
    <svg viewBox="0 0 34 34" aria-hidden="true"><circle cx="17" cy="17" r="15" fill="none" stroke="#fff" stroke-width="2.4"/><path d="M11.5 9.5c1-.8 2-.6 2.6.4l1.4 2.6c.4.8.2 1.6-.5 2.1l-1 .7c.9 2.2 2.4 3.8 4.6 4.8l.8-1c.5-.7 1.4-.9 2.1-.4l2.5 1.5c.9.6 1.1 1.7.3 2.5l-1.2 1.2c-1.2 1.2-3.2 1.2-5.4-.1-3.4-2-6-5-7.4-8.6-.7-2-.4-3.6.6-4.6z" fill="#fff"/></svg>
    <span>555-014-2291</span>
  </div>

  <div class="abs footer-links">
    <span class="social-square"></span>
    <span class="social-square"></span>
    <span class="website">www.tarnwickbuildco.example</span>
  </div>
</main>
</body>
</html>
```